Brochure Design Project - Innovative Service for Pharma Industry

Our start up is based in Germany, near Munich and we provide an innovative Service for the pharma industry. We develop product trainings and general trainings online. The adressed audience for these trainings are pharmacies and medics. The parma industry could increase the number of trainings, while saving money (incl a success guarantee). Our (not yet finnished) corporate page can be reviewed here: www.veltrano.biz, our 'product & service' page is www.medolearnix.com. The color code should be leaned towards the corporate page.

The brochure should be send to decision makers in the pharma industry and rise the interest in innovative service. Seriousity should meet modern & clear design.Something eye cathing on the front page might be required.
Updates

Target Market(s)

Usually more conservative decision makers within the pharma industry

Industry/Entity Type

Industry

Requirements
Must have
• Conceptional design for an brochure (Din A4 size) of approx 6-8 pages, that capture the key messages (exact content would be filled / provided from us)
Nice to have
• Implementing some of the pics / phrases on the home page www.veltano.biz could be maybe nice. How about a personal statement from the founder combined with a pic(pic attached)? Both is no must....

```html
<!DOCTYPE html>
<html lang="de">
<head>
<meta charset="utf-8">
<title>veltrano – Broschüre</title>
<link rel="stylesheet" href="https://fonts.googleapis.com/css2?family=Arimo:wght@400;700&family=Gelasio:wght@400&display=swap">
<style>
  :root{
    --black:#000;
    --white:#fff;
    --red:#c4000a;
    --red-light:#f3343a;
    --orange:#e84a12;
    --grey-bar:#9b9b9b;
    --grey-ring:#5f646b;
    --grey-text:#8a8a8a;
    --ink:#111;
  }
  html,body{margin:0;padding:0;width:1200px;height:860px;overflow:hidden;background:var(--black);}
  .stage{position:absolute;left:0;top:0;width:1270px;height:910px;transform:scale(0.9449);transform-origin:0 0;font-family:"Arimo",Arial,sans-serif;}
  .label{position:absolute;top:12px;color:var(--white);font-size:11px;letter-spacing:.2px;}
  .label--inner{left:334px;}
  .label--cover{left:885px;}

  .page{position:absolute;top:34px;width:596px;height:842px;background:var(--white);overflow:hidden;}
  .page--inner{left:43px;}
  .page--cover{left:639px;border-left:1px solid #888;box-sizing:border-box;}

  .sidebar-red{position:absolute;left:0;top:0;width:62px;height:416px;background:linear-gradient(90deg,var(--red) 0%,var(--red) 40%,var(--red-light) 100%);}
  .sidebar-grey{position:absolute;left:0;top:426px;width:62px;height:416px;background:var(--grey-bar);}
  .sidebar-url{position:absolute;left:31px;top:326px;transform:translate(-50%,-50%) rotate(-90deg);color:var(--white);font-size:13px;letter-spacing:3px;white-space:nowrap;}

  .brand{position:absolute;left:112px;top:150px;width:150px;display:flex;align-items:center;gap:8px;}
  .brand__dot{width:14px;height:14px;border-radius:50%;background:var(--orange);}
  .brand__name{color:var(--orange);font-size:28px;font-weight:400;}

  .heading{position:absolute;margin:0;font-family:"Gelasio",Georgia,serif;font-weight:400;color:var(--red);}
  .heading--service{left:289px;top:100px;font-size:22px;}
  .heading--mehrwerte{left:107px;top:422px;font-size:24px;}
  .copy{position:absolute;margin:0;color:var(--grey-text);font-size:10px;line-height:13px;}
  .copy strong{display:block;color:#777;font-weight:700;}

  .cover-art{position:absolute;left:0;top:0;}
  .cover-url{position:absolute;left:84px;top:167px;font-family:"Gelasio",Georgia,serif;font-size:16px;color:var(--ink);}
  .cover-brand{position:absolute;left:294px;top:184px;width:140px;display:flex;justify-content:center;align-items:center;gap:8px;}
  .cover-claim{position:absolute;left:103px;top:706px;margin:0;width:360px;font-size:17px;line-height:22px;color:var(--ink);}
</style>
</head>
<body>
<div class="stage">
  <div class="label label--inner">INNER PAGE</div>
  <div class="label label--cover">COVER</div>

  <section class="page page--inner">
    <div class="sidebar-red"></div>
    <div class="sidebar-grey"></div>
    <div class="sidebar-url">www.veltrano.biz</div>

    <div class="brand"><span class="brand__dot"></span><span class="brand__name">veltrano</span></div>

    <h2 class="heading heading--service">service</h2>
    <p class="copy" style="left:289px;top:136px;width:260px;">veltrano entwickelt neuartige E-Learning Konzepte und bietet diese als Plattform für speziell definierte Zielmärkte und deren gesamte Industrie an.</p>
    <p class="copy" style="left:289px;top:188px;width:265px;">Wenn Ihr Unternehmen in der Pharmazeutischen Entwicklung tätig ist, gehören Sie zu unseren Top-Zielkunden. Unsere CLOUD basierenden E-Learning Lösungen erlauben es Ihnen sich auf das Wesentliche zu konzentrieren: auf die Entwicklung neuer Produkte. Wir übernehmen das Produkttraining.</p>
    <p class="copy" style="left:104px;top:278px;width:450px;">Hierbei fokussieren wir uns primär auf vertikale Märkte aus Industrien deren Produkten einen hohen Erklärungs- und Trainingsbedarf haben und zugleich über eine breite Kundenbasis verfügen. Die Pharmaindustrie ist unser bestes Beispiel für einen solchen Markt. Für unsere Kunden dient die Produktschulung als wichtiges Mittel des Unternehmenerfolges. Die zeitgleiche Umsetzung und das Adressieren der Kundenbreite gestaltet sich jedoch schwierig und ist mit hohem Personal- und Kostenaufwand verbunden. veltrano bietet umfassende E-Learning Lösungen, welche nicht nur Mehrwerte für alle Beteiligten schaffen sondern insbesonders für unsere Kunden Umsatzwachstum bei höherer Effizienz gewährleisten. Nutzen Sie die neuen Chancen die sich Ihnen eröffnen.</p>

    <h2 class="heading heading--mehrwerte">mehrwerte</h2>
    <p class="copy" style="left:107px;top:466px;width:450px;">Wir sind davon überzeugt, das Produkte und Services Mehrwerte für Kunden bieten müssen um daraus Erfolg generieren zu können. Verschaffen Sie sich einen Überblick über unsere Vorteile welche Sie in diesem Umfang nur bei uns finden können.</p>
    <p class="copy" style="left:107px;top:516px;width:450px;"><strong>Flexibel sein</strong><br>Als unser Kunde haben Sie mit Hilfe unseres Services vollste Flexibilität was den Einsatz Ihrer Ressourcen, Investitionen oder die Zielkunden in Bezug auf Produktschulungen angeht. Sie sind an nichts gebunden, haben keine fixen Kosten und Nutzen unsere Dienste wann immer Sie uns benötigen. Sie müssen keinen eigenen oder externen Mitarbeiter schulen, damit diese Ihre Kunden schulen. Der Anzahl Ihrer gewünschten Schulungen und auch nicht gewünschten Trainingsteilnehmer sind keinerlei Grenzen gesetzt – da wir CLOUD Technologien einsetzen sind unsere Dienste unbegrenzt scallierbar</p>
    <p class="copy" style="left:107px;top:640px;width:450px;"><strong>Investitionen messbar machen</strong><br>Die elektronische Erfassung über die Teilnahme, abgeschlossener Tests sowie deren Ergebnisse sorgen für eine lückenlose Belegung der durchgeführten Trainings und der Resultate.Sämtliche Details über jedes Trainingsmodul kann mit unserem Kunden erläutert und dokumentiert werden. Auf die Einhaltung von Datenschutzrichtlinien wir hierbei natürlich strengstens geachtet. Die Nutzung unserer Technologien erlaubt Ihrem Unternehmen erstmals die Effektivität Ihrer eingesetzten Mittel zu belegen und den ROI zu überprüfen. Ihr Controlling und Ihre Shareholder werden es Ihnen danken.</p>
  </section>

  <section class="page page--cover">
    <svg class="cover-art" width="596" height="842" viewBox="0 0 596 842" aria-hidden="false">
      <defs>
        <linearGradient id="band" x1="0" x2="1" y1="0" y2="0">
          <stop offset="0" stop-color="#b5000a"/><stop offset=".7" stop-color="#c4000a"/><stop offset="1" stop-color="#f3343a"/>
        </linearGradient>
        <linearGradient id="sweep" x1="0" x2="1" y1="1" y2="0">
          <stop offset="0" stop-color="#c9c9c9"/><stop offset=".5" stop-color="#f2f2f2"/><stop offset="1" stop-color="#dcdcdc"/>
        </linearGradient>
        <radialGradient id="photoMan" cx=".5" cy=".45" r=".6">
          <stop offset="0" stop-color="#e6d27a"/><stop offset=".5" stop-color="#3d5f92"/><stop offset="1" stop-color="#4a8fd0"/>
        </radialGradient>
        <radialGradient id="photoEye" cx=".5" cy=".5" r=".6">
          <stop offset="0" stop-color="#4fa86a"/><stop offset=".6" stop-color="#8a7a3a"/><stop offset="1" stop-color="#1a1a1a"/>
        </radialGradient>
        <radialGradient id="photoWoman" cx=".5" cy=".5" r=".6">
          <stop offset="0" stop-color="#d9b9a4"/><stop offset=".7" stop-color="#b7a7a0"/><stop offset="1" stop-color="#6a5a5a"/>
        </radialGradient>
      </defs>
      <rect x="0" y="198" width="596" height="644" fill="url(#band)"/>
      <path d="M0,842 C20,610 180,330 596,240 L596,842 Z" fill="url(#sweep)"/>
      <rect x="67" y="165" width="2" height="63" fill="var(--red)"/>

      <circle cx="364" cy="201" r="150" fill="var(--grey-ring)"/>
      <circle cx="364" cy="201" r="134" fill="var(--white)"/>

      <circle cx="181" cy="466" r="172" fill="var(--white)"/>
      <g role="img" aria-label="Foto: Mann im Anzug, mit gelbem Absperrband umwickelt">
        <circle cx="181" cy="466" r="160" fill="url(#photoMan)"/>
      </g>

      <circle cx="434" cy="386" r="110" fill="var(--white)"/>
      <g role="img" aria-label="Foto: Nahaufnahme eines Auges hinter grün spiegelnder Schutzbrille">
        <circle cx="434" cy="386" r="97" fill="url(#photoEye)"/>
      </g>

      <circle cx="406" cy="571" r="114" fill="var(--grey-ring)"/>
      <g role="img" aria-label="Foto: Frau streckt die Hand abwehrend zur Kamera">
        <circle cx="406" cy="571" r="98" fill="url(#photoWoman)"/>
      </g>
    </svg>

    <div class="cover-url">www.veltano.biz</div>
    <div class="cover-brand"><span class="brand__dot"></span><span class="brand__name">veltrano</span></div>
    <p class="cover-claim">veltrano entwickelt neuartige E-Learning Konzepte und bietet diese als Plattform für speziell definierte Zielmärkte und deren gesamte Industrie an.</p>
  </section>
</div>
</body>
</html>
```